Webdesign Birkenhainer Kinderstuben e.V.
Petra Lohmann
Sehr modernes und passendes Layout für das geplante Projekt, Kunde ist sehr zufrieden
Zielgruppe
Verein für Kinder und Jugendliche / Jugendclubs und Kindertagesstätten, sowie Schulsozialarbeit
Aufgabenstellung
- Klares und übersichtliches Desgin
- nicht zu verspielt
- informativ
- leichte Naviagtion
- das Design der alten Webseite soll NICHT kopiert werden
- die Farbe Blau aus der alten Seite soll sich wiederfinden
- Das Logo bunt und schwarz/Weiß soll eingebunden werden
- Bildmaterial Kinder im Kindergarten, Jugendliche im Jugendclub, Sozialarbeit mit Jugendliche, Betreuung im Schulhort
- Social Media Kanäle Instagram & Facebook sind vorhanden und können als Gestaltungsinstrument mit verwendet werden

```html
<!DOCTYPE html>
<html lang="de">
<head>
<meta charset="utf-8">
<title>Birkenhainer Kinderstuben e.V. – Webdesign</title>
<link href="https://fonts.googleapis.com/css2?family=Poppins:wght@400;500;600;700&display=swap" rel="stylesheet">
<style>
:root{
  --stage:#ffffff;
  --page:#ffffff;
  --ink:#1f1f24;
  --muted:#55565c;
  --grey-head:#7a7b80;
  --soft:#f0f0f2;
  --blue:#6fa8c9;
  --blue-band:#8db8d6;
  --blue-text:#5f9dc2;
  --yellow:#f7df3f;
  --crimson:#a51a45;
  --footer:#242022;
  --accent-line:#c8254f;
  --badge-green:#3f8f4f;
}
*{box-sizing:border-box;margin:0;padding:0}
html,body{width:1200px;height:3698px;overflow:hidden;background:var(--stage);font-family:"Poppins",sans-serif;color:var(--ink)}
.page{position:absolute;left:70px;top:29px;width:1060px;background:var(--page);box-shadow:0 4px 24px rgba(0,0,0,.12);overflow:hidden}
section,header,footer{position:relative;width:1060px;overflow:hidden}

/* header */
.site-header{height:83px;display:flex;align-items:center;padding:0 118px 0 122px;justify-content:space-between;background:#fff}
.brand{display:flex;align-items:center;gap:8px;font-size:13px;font-weight:600;color:var(--ink);line-height:1.15;width:140px}
.brand-dot{width:14px;height:14px;border-radius:50%;background:var(--crimson);flex:none}
.nav{display:flex;gap:20px;font-size:10.5px;font-weight:600;text-transform:uppercase;letter-spacing:.2px}
.nav a{color:var(--ink);text-decoration:none;padding-bottom:5px}
.nav a.active{border-bottom:2px solid var(--accent-line)}

/* photo placeholders */
.photo{position:absolute}
.hero-photo{inset:0;background:
  radial-gradient(ellipse 30% 45% at 82% 45%,rgba(196,170,140,.55),rgba(0,0,0,0) 70%),
  radial-gradient(ellipse 25% 40% at 50% 30%,rgba(120,105,95,.5),rgba(0,0,0,0) 70%),
  linear-gradient(100deg,#2f2b29 0%,#4b4440 40%,#6e625a 70%,#857a71 100%)}
.hero-shade{position:absolute;inset:0;background:linear-gradient(90deg,rgba(0,0,0,.5),rgba(0,0,0,.05))}

/* hero */
.hero{height:590px}
.hero-content{position:absolute;left:118px;top:160px;color:#fff}
.hero h1{font-size:58px;font-weight:500;line-height:1.05;letter-spacing:-.5px}
.hero p{margin-top:32px;width:450px;font-size:14px;line-height:24px}
.btn-row{display:flex;gap:28px;margin-top:42px}
.btn{display:flex;align-items:center;justify-content:center;width:170px;height:44px;border-radius:4px;font-size:14px;font-weight:500;color:#fff;text-decoration:none}
.btn-blue{background:var(--blue)}
.btn-ghost{border:2px solid #fff}

/* about */
.about{height:683px;background:var(--soft)}
.about-text{position:absolute;left:118px;top:78px;width:430px}
.eyebrow{font-size:21px;font-weight:500;color:var(--grey-head);text-transform:uppercase}
.about h2{margin-top:20px;font-size:21px;font-weight:600;line-height:30px}
.about p{margin-top:24px;font-size:13.5px;line-height:24px;color:var(--muted)}
.about p + p{margin-top:22px}
.stats{display:flex;gap:80px;margin-top:32px}
.stat-num{font-size:34px;font-weight:600;color:var(--blue-text);line-height:1}
.stat-label{margin-top:10px;font-size:13px;font-weight:600;color:var(--blue-text);line-height:1.1;width:140px}
.about .btn{margin-top:64px}
.about-photo{left:590px;top:74px;width:470px;height:549px;background:
  linear-gradient(180deg,#d9dee1 0%,#cdd3d6 30%,#c4b38c 31%,#b9a77f 62%,#6f6c66 63%,#5b5955 100%)}

/* news */
.news{height:465px;background:#fff}
.news h2{position:absolute;top:60px;width:100%;text-align:center;font-size:21px;font-weight:500;color:var(--grey-head);text-transform:uppercase}
.cards{position:absolute;left:118px;top:130px;display:flex;gap:24px}
.card{width:259px;height:292px;background:#fff;box-shadow:0 2px 10px rgba(0,0,0,.1);position:relative}
.card-img{height:183px}
.img-kids{background:linear-gradient(180deg,#f1f1f2 0%,#e6ddd4 60%,#d6b793 100%)}
.img-party{background:linear-gradient(180deg,#d6b27a 0%,#e3c28a 55%,#c4905a 100%)}
.img-beach{background:linear-gradient(180deg,#a9cbe4 0%,#c9d8e2 40%,#dcc7a6 60%,#cdb08a 100%)}
.card-date{margin:22px 0 0 22px;font-size:11px;color:var(--muted)}
.card-title{margin:16px 0 0 22px;font-size:14px;line-height:22px;color:var(--ink)}
.card-title b{font-weight:600}
.chev{position:absolute;right:20px;bottom:18px;width:12px;height:14px}

/* kitas */
.kitas{height:477px;background:var(--blue-band);color:#fff}
.kitas h2{position:absolute;left:118px;top:64px;font-size:21px;font-weight:600}
.kitas p{position:absolute;left:118px;top:108px;width:520px;font-size:13.5px;line-height:24px}
.slider-arrows{position:absolute;left:893px;top:132px;display:flex;gap:10px}
.kita-row{position:absolute;left:188px;top:188px;display:flex;gap:24px}
.kita-card{width:329px;height:220px;border-radius:3px;position:relative;overflow:hidden;flex:none}
.kita-1{background:linear-gradient(180deg,#6d9ad0 0%,#a9c0d8 35%,#d6c7a6 36%,#c9b693 65%,#5f5a54 100%)}
.kita-2{background:linear-gradient(180deg,#b3c3cf 0%,#9fb3bd 25%,#7c9565 26%,#65804f 60%,#4a5545 100%)}
.kita-3{background:linear-gradient(180deg,#7a9a5e 0%,#5b7a45 55%,#3b4539 100%)}
.kita-shade{position:absolute;inset:0;background:linear-gradient(180deg,rgba(0,0,0,0) 40%,rgba(0,0,0,.55) 100%)}
.kita-info{position:absolute;left:20px;bottom:20px;color:#fff;white-space:nowrap}
.kita-info h3{font-size:13.5px;font-weight:600;line-height:17px}
.kita-info span{display:flex;align-items:center;gap:8px;margin-top:12px;font-size:9.5px;font-weight:500}

/* school social work */
.school{height:625px}
.school-photo{inset:0;background:
  radial-gradient(ellipse 22% 55% at 62% 60%,rgba(150,70,55,.45),rgba(0,0,0,0) 70%),
  radial-gradient(ellipse 20% 55% at 88% 60%,rgba(90,80,70,.5),rgba(0,0,0,0) 70%),
  linear-gradient(90deg,#2e2d2b 0%,#46443f 45%,#5e554b 75%,#3f3b37 100%)}
.school-shade{position:absolute;inset:0;background:linear-gradient(90deg,rgba(0,0,0,.45),rgba(0,0,0,.05))}
.school-content{position:absolute;left:118px;top:80px;color:#fff}
.school h2{font-size:21px;font-weight:600;color:var(--yellow)}
.school p{margin-top:20px;width:330px;font-size:13.5px;line-height:24px}
.loc-list{position:absolute;left:118px;top:308px;display:flex;flex-direction:column;gap:22px}
.loc-btn{width:329px;height:65px;background:var(--yellow);border-radius:3px;display:flex;align-items:stretch;color:var(--ink)}
.loc-main{flex:1;padding:14px 0 0 24px}
.loc-main b{display:block;font-size:13.5px;font-weight:500}
.loc-main span{display:flex;align-items:center;gap:10px;margin-top:6px;font-size:9.5px;font-weight:500}
.loc-arrow{width:86px;border-left:1px solid rgba(0,0,0,.1);display:flex;align-items:center;justify-content:center}
.partner-badge{position:absolute;left:928px;top:522px;width:72px;height:100px;background:#fff;display:flex;align-items:flex-end;justify-content:center;padding-bottom:14px}
.partner-badge i{display:block;width:44px;height:44px;background:var(--badge-green);border-radius:2px}

/* youth */
.youth{height:449px;background:#fff}
.youth h2{position:absolute;left:118px;top:62px;font-size:21px;font-weight:500;color:var(--grey-head);text-transform:uppercase}
.youth p{position:absolute;left:118px;top:120px;width:540px;font-size:13.5px;line-height:24px;color:var(--muted)}
.youth-grid{position:absolute;left:118px;top:211px;display:grid;grid-template-columns:259px 259px;gap:18px 24px}
.red-btn{height:83px;background:var(--crimson);border-radius:3px;color:#fff;display:flex;align-items:center;justify-content:space-between;padding:0 22px;font-size:13.5px;font-weight:500;line-height:19px}
.youth-photo{left:672px;top:150px;width:364px;height:299px;border-radius:4px 4px 0 0;background:linear-gradient(160deg,#f3d36a 0%,#e79a4a 40%,#c9503f 70%,#7b9cbc 100%)}

/* footer */
.site-footer{height:268px;background:var(--footer);color:#fff}
.foot-col{position:absolute;top:34px;font-size:9.5px;line-height:19px}
.foot-col h4{font-size:10.5px;font-weight:600;margin-bottom:12px;text-transform:uppercase}
.foot-contact{left:118px}
.foot-links{left:361px}
.foot-links a{display:block;color:#fff;text-decoration:none;margin-bottom:4px}
.foot-brand{position:absolute;left:750px;top:70px;display:flex;align-items:center;gap:10px;font-size:17px;font-weight:600;line-height:1.2;width:200px}
.foot-brand .brand-dot{background:#fff}
.socials{position:absolute;left:870px;top:168px;display:flex;gap:10px}
.socials span{width:12px;height:12px;border-radius:50%;background:#fff}
.copyright{position:absolute;top:236px;width:100%;text-align:center;font-size:9.5px;font-weight:500}
</style>
</head>
<body>
<div class="page">

  <header class="site-header">
    <div class="brand"><span class="brand-dot"></span>Birkenhainer Kinderstuben e.V.</div>
    <nav class="nav">
      <a class="active" href="#">Über uns</a>
      <a href="#">Aktuelles</a>
      <a href="#">Kitas &amp; Hort</a>
      <a href="#">Schulsozialarbeit</a>
      <a href="#">Kinder- &amp; Jugendarbeit</a>
      <a href="#">Kontakt</a>
    </nav>
  </header>

  <section class="hero">
    <div class="photo hero-photo" role="img" aria-label="Foto: Kinder lernen mit einer Betreuerin im Klassenraum"></div>
    <div class="hero-shade"></div>
    <div class="hero-content">
      <h1>Verein Für Kinder<br>Und Jugendliche</h1>
      <p>Lorem Ipsum Dolor Sit Amet, Consectetur Adipiscing Elit, Sed Do Eiusmod Tempor Incididunt Ut Labore Et Dolore Magna Aliqua.</p>
      <div class="btn-row">
        <a class="btn btn-blue" href="#">Mehr Erfaren</a>
        <a class="btn btn-ghost" href="#">Über Uns</a>
      </div>
    </div>
  </section>

  <section class="about">
    <div class="about-text">
      <div class="eyebrow">Über Uns</div>
      <h2>Vorstellung Des Vereins Birkenhainer Kinderstuben</h2>
      <p>Der Birkenhainer Kinderstuben E.V. Wurde Am <b>16.11.1992</b> Gegründet. Wir Sind Ein Gemeinnütziger Verein Und Anerkannter Träger Der Freien Jugendhilfe. Unser Betätigungsfelder Liegen In Den Landkreisen Nordtal Sowie Mittelauen.</p>
      <p>Der Ehrenamtliche Vorstand Besteht Aus 4 Mitgliedern. Vorstandsvorsitzender Ist Herr Thomas Brenner. Stellvertretende Vorsitzende Ist Frau Sabine Kroll</p>
      <div class="stats">
        <div><div class="stat-num">44</div><div class="stat-label">Festangestellte</div></div>
        <div><div class="stat-num">2</div><div class="stat-label">Ehrenamtliche Mitarbeiterinnen</div></div>
      </div>
      <a class="btn btn-blue" href="#">Über Uns</a>
    </div>
    <div class="photo about-photo" role="img" aria-label="Foto: Vereinsgebäude mit heller Fassade und großen Fenstern"></div>
  </section>

  <section class="news">
    <h2>Aktuelles</h2>
    <div class="cards">
      <article class="card">
        <div class="card-img img-kids" role="img" aria-label="Foto: Kinder packen einen Spendenkarton"></div>
        <div class="card-date">01./02.04.25</div>
        <div class="card-title">Benefizkonzert<br><b>'Kinder Helfen Kindern'</b></div>
        <svg class="chev" viewBox="0 0 12 14"><path d="M4 2l5 5-5 5" fill="none" stroke="#6fa8c9" stroke-width="1.6"/></svg>
      </article>
      <article class="card">
        <div class="card-img img-party" role="img" aria-label="Foto: Kinder feiern ein Fest mit Ballons"></div>
        <div class="card-date">07.06.25</div>
        <div class="card-title"><b>Kinderfest Birkenhain</b></div>
        <svg class="chev" viewBox="0 0 12 14"><path d="M4 2l5 5-5 5" fill="none" stroke="#6fa8c9" stroke-width="1.6"/></svg>
      </article>
      <article class="card">
        <div class="card-img img-beach" role="img" aria-label="Foto: Kinder spielen am Sandstrand"></div>
        <div class="card-date">22.06.25</div>
        <div class="card-title"><b>Inselgig Birkenhain</b></div>
        <svg class="chev" viewBox="0 0 12 14"><path d="M4 2l5 5-5 5" fill="none" stroke="#6fa8c9" stroke-width="1.6"/></svg>
      </article>
    </div>
  </section>

  <section class="kitas">
    <h2>KITAS &amp; HORT</h2>
    <p>Lorem Ipsum Dolor Sit Amet, Consectetur Adipiscing Elit, Sed Do Eiusmod Tempor Incididunt Ut Labore Et Dolore Magna Aliqua.</p>
    <div class="slider-arrows">
      <svg width="10" height="14" viewBox="0 0 10 14"><path d="M7 2L2 7l5 5" fill="none" stroke="#fff" stroke-width="1.6"/></svg>
      <svg width="10" height="14" viewBox="0 0 10 14"><path d="M3 2l5 5-5 5" fill="none" stroke="#fff" stroke-width="1.6"/></svg>
    </div>
    <div class="kita-row">
      <div class="kita-card kita-1" role="img" aria-label="Foto: Kindertagesstätte Sternschnuppe">
        <div class="kita-shade"></div>
        <div class="kita-info"><h3>Kindertagesstätte Sternschnuppe<br>In Talheim</h3>
          <span><svg width="9" height="11" viewBox="0 0 9 11"><path d="M4.5 10S1 6.3 1 4.2a3.5 3.5 0 017 0C8 6.3 4.5 10 4.5 10z" fill="none" stroke="#fff"/><circle cx="4.5" cy="4.2" r="1.2" fill="#fff"/></svg>Sternschnuppe, Gartenstr. 12 A</span></div>
      </div>
      <div class="kita-card kita-2" role="img" aria-label="Foto: Luftbild Kinderhaus Pusteblume">
        <div class="kita-shade"></div>
        <div class="kita-info"><h3>Kindertagesstätte Erlenbach<br>'Kinderhaus Pusteblume'</h3>
          <span><svg width="9" height="11" viewBox="0 0 9 11"><path d="M4.5 10S1 6.3 1 4.2a3.5 3.5 0 017 0C8 6.3 4.5 10 4.5 10z" fill="none" stroke="#fff"/><circle cx="4.5" cy="4.2" r="1.2" fill="#fff"/></svg>Erlenbach, Am Anger 4</span></div>
      </div>
      <div class="kita-card kita-3" role="img" aria-label="Foto: Hortgebäude zwischen Bäumen">
        <div class="kita-shade"></div>
        <div class="kita-info"><h3>Hort 'Wolkenland'<br>An Der Lindengrundschule</h3>
          <span><svg width="9" height="11" viewBox="0 0 9 11"><path d="M4.5 10S1 6.3 1 4.2a3.5 3.5 0 017 0C8 6.3 4.5 10 4.5 10z" fill="none" stroke="#fff"/><circle cx="4.5" cy="4.2" r="1.2" fill="#fff"/></svg>Talheim, Auental</span></div>
      </div>
    </div>
  </section>

  <section class="school">
    <div class="photo school-photo" role="img" aria-label="Foto: Jugendliche mit Rucksäcken auf dem Weg zur Schule"></div>
    <div class="school-shade"></div>
    <div class="school-content">
      <h2>SCHULSOZIALARBEIT</h2>
      <p>Der Verein Birkenhainer Kinderstuben Ist An Den Oberschulen In Birkenhain Und Talheim Sowie An Der Grundschule Birkenhain Mit Schulsozialarbeit Engagiert. Für Nähere Informationen Wählen Sie Bitte Einen Standort.</p>
    </div>
    <div class="loc-list">
      <a class="loc-btn"><div class="loc-main"><b>Grundschule Birkenhain</b><span><svg width="9" height="11" viewBox="0 0 9 11"><path d="M4.5 10S1 6.3 1 4.2a3.5 3.5 0 017 0C8 6.3 4.5 10 4.5 10z" fill="none" stroke="#1f1f24"/><circle cx="4.5" cy="4.2" r="1.2" fill="#1f1f24"/></svg>Birkenhain, Lindenallee 23</span></div><div class="loc-arrow"><svg width="10" height="14" viewBox="0 0 10 14"><path d="M3 2l5 5-5 5" fill="none" stroke="#1f1f24" stroke-width="1.6"/></svg></div></a>
      <a class="loc-btn"><div class="loc-main"><b>Oberschule Birkenhain</b><span><svg width="9" height="11" viewBox="0 0 9 11"><path d="M4.5 10S1 6.3 1 4.2a3.5 3.5 0 017 0C8 6.3 4.5 10 4.5 10z" fill="none" stroke="#1f1f24"/><circle cx="4.5" cy="4.2" r="1.2" fill="#1f1f24"/></svg>Birkenhain, Schulweg 9</span></div><div class="loc-arrow"><svg width="10" height="14" viewBox="0 0 10 14"><path d="M3 2l5 5-5 5" fill="none" stroke="#1f1f24" stroke-width="1.6"/></svg></div></a>
      <a class="loc-btn"><div class="loc-main"><b>Oberschule Talheim</b><span><svg width="9" height="11" viewBox="0 0 9 11"><path d="M4.5 10S1 6.3 1 4.2a3.5 3.5 0 017 0C8 6.3 4.5 10 4.5 10z" fill="none" stroke="#1f1f24"/><circle cx="4.5" cy="4.2" r="1.2" fill="#1f1f24"/></svg>Talheim, Mühlenstr. 103</span></div><div class="loc-arrow"><svg width="10" height="14" viewBox="0 0 10 14"><path d="M3 2l5 5-5 5" fill="none" stroke="#1f1f24" stroke-width="1.6"/></svg></div></a>
    </div>
    <div class="partner-badge" role="img" aria-label="Förderhinweis des Landes"><i></i></div>
  </section>

  <section class="youth">
    <h2>Kinder- &amp; Jugendarbeit</h2>
    <p>Lorem Ipsum Dolor Sit Amet, Consectetur Adipiscing Elit, Sed Do Eiusmod Tempor Incididunt Ut Labore Et Dolore Magna Aliqua.</p>
    <div class="youth-grid">
      <a class="red-btn">JUGENDladen Birkenhain<svg width="10" height="14" viewBox="0 0 10 14"><path d="M3 2l5 5-5 5" fill="none" stroke="#fff" stroke-width="1.6"/></svg></a>
      <a class="red-btn">Jugendclub Talheim<svg width="10" height="14" viewBox="0 0 10 14"><path d="M3 2l5 5-5 5" fill="none" stroke="#fff" stroke-width="1.6"/></svg></a>
      <a class="red-btn">Schulclub<svg width="10" height="14" viewBox="0 0 10 14"><path d="M3 2l5 5-5 5" fill="none" stroke="#fff" stroke-width="1.6"/></svg></a>
      <a class="red-btn">Mobile Jugendarbeit/<br>Streetwork Talheim<svg width="10" height="14" viewBox="0 0 10 14"><path d="M3 2l5 5-5 5" fill="none" stroke="#fff" stroke-width="1.6"/></svg></a>
    </div>
    <div class="photo youth-photo" role="img" aria-label="Foto: drei Kinder mit Helm, Werkzeug und Tablet vor bunten Farbflecken"></div>
  </section>

  <footer class="site-footer">
    <div class="foot-col foot-contact">
      <h4>Kontakt</h4>
      <b>Birkenhainer Kinderstuben e.V.</b><br>
      Am Birkenweg 8<br>
      09999 Birkenhain<br>
      <div style="margin-top:8px">Telefon: 03712 - 5550101</div>
      <div style="margin-top:4px">Fax: 03712 - 5550151</div>
      <div style="margin-top:4px">info@birkenhainer-kinderstuben.de</div>
    </div>
    <div class="foot-col foot-links">
      <h4>Quicklinks</h4>
      <a href="#">Über uns</a>
      <a href="#">Aktuelles</a>
      <a href="#">Kitas &amp; Hort</a>
      <a href="#">Schulsozialarbeit</a>
      <a href="#">Kinder- &amp; Jugendarbeit</a>
    </div>
    <div class="foot-brand"><span class="brand-dot"></span>Birkenhainer Kinderstuben e.V.</div>
    <div class="socials" aria-label="Social Media"><span></span><span></span><span></span></div>
    <div class="copyright">©2025. Birkenhainer Kinderstuben e.V. All rights reserved</div>
  </footer>

</div>
</body>
</html>
```